Revise Three Graphics for Company Careers website.

We have a need to find an alternative artistic approach to revising three graphics currently used on a growing companies careers/job website.
- The new art for attached graphics (named graphic #1, #2, and #3) should be clean, professional and easy to read.
- The art representing these three pieces should share common artistic elements and not necessarily look like three differently branded pieces.
- The careers site is shared between two related companies, so the colors used should complement the colors of two companies (whose logos are attached).
- Logos can be used as knock-outs if needed.
Note: Graphic #3 (currently a set of boxes 2x3) needs two additional boxes with the following copy:
- Art and Science of Communication
- Supervising 101
Lastly, Graphic #4 we need to be put into the same color font used in the two company logos. That's it!

```html
<!DOCTYPE html>
<html lang="en">
<head>
<meta charset="UTF-8">
<title>Development Programs</title>
<link href="https://fonts.googleapis.com/css2?family=Open+Sans:wght@400;600&display=swap" rel="stylesheet">
<style>
  :root {
    --page-center: #ffffff;
    --page-edge: #e6e6e6;
    --frame: #9a9a9a;
    --navy: #144b8a;
    --red: #f0203b;
    --lime: #9bcc00;
    --sky: #4bcde6;
    --ring: #3aabbf;
    --ink-navy: #1b3c6c;
    --ink-dark: #2e2e2e;
    --white: #ffffff;
  }
  * { margin: 0; padding: 0; box-sizing: border-box; }
  html, body { width: 849px; height: 1200px; overflow: hidden; }
  body {
    font-family: "Open Sans", sans-serif;
    background: var(--page-edge);
  }
  .canvas {
    position: relative;
    width: 849px;
    height: 1200px;
    background: radial-gradient(ellipse at 50% 45%, var(--page-center) 0%, #f6f6f6 50%, var(--page-edge) 100%);
    border: 1px solid var(--frame);
  }
  .program {
    position: absolute;
    width: 178px;
    height: 178px;
    margin: -89px 0 0 -89px;
    border-radius: 50%;
    display: flex;
    align-items: center;
    justify-content: center;
    text-align: center;
    padding: 0 10px;
    font-size: 18px;
    line-height: 1.42;
    box-shadow: 3px 5px 10px rgba(0,0,0,0.28);
  }
  .program--filled {
    color: var(--white);
    font-weight: 600;
    letter-spacing: -0.3px;
    text-shadow: 0 1px 2px rgba(0,0,0,0.25);
    border: 3px solid #dcdcdc;
  }
  .program--outline {
    background: var(--white);
    border: 4px solid var(--ring);
    color: var(--ink-navy);
  }
  .program--navy { background: var(--navy); }
  .program--red { background: var(--red); }
  .program--lime { background: var(--lime); }
  .program--sky { background: var(--sky); border-color: var(--sky); }
  .program--dark-ink { color: var(--ink-dark); }
</style>
</head>
<body>
  <main class="canvas">
    <div class="program program--filled program--navy" style="left:127px; top:505px;">Scientific Lunch and Learns</div>
    <div class="program program--outline" style="left:317px; top:505px;">Statistics in Pharmaceutical Development Workshop</div>
    <div class="program program--filled program--red" style="left:517px; top:505px;">Conferences and Seminars</div>
    <div class="program program--outline" style="left:707px; top:505px;">Leadership Development</div>

    <div class="program program--outline" style="left:124px; top:696px;">Creating the Right Team Workshop</div>
    <div class="program program--filled program--lime" style="left:315px; top:696px;">Project Management Training</div>
    <div class="program program--outline program--dark-ink" style="left:529px; top:696px;">Art and Science of Communication</div>
    <div class="program program--filled program--sky" style="left:720px; top:696px;">Supervising 101</div>
  </main>
</body>
</html>
```